Restoration Specialist in need of business card designs

One side of the business card is a bathroom ripped out down to the studs with just a sink and toilet and then the other side is the bathroom (same sink and toilet) but put back together. Like a before and after on each side behind our information. Stand out, hard to forget, business cards for my restoration company. I want a unique concept all together.
Must include in no particular order:
our business name "Summit Renewals"
Possible Logo for a restoration company
Owner; Dennis Moravec
410-386-7294
dmoravec@summitrenewalsqx.example
SummitRenewalsQX.example (our company website) BUT I am open to any and all designs and options.

Target Market(s)

Customers, Men in the mitigation, plumbing, electrical, HVAC, Roofing, insurance companies

Industry/Entity Type

Restoration/ construction

Contact Information for Business Card

Must include in no particular order: our business name "Summit Renewals" Owner; Dennis Moravec 410-386-7294 dmoravec@summitrenewalsqx.example SummitRenewalsQX.example (our company website) MAY include a list of our services: Residential~ Emergency Response ~ Board- up~ Complete Restoration

Font styles to use
Serif

Colors
0054AA
0677BA
7BADD7
CADEEF
E8F1F8
F0912C
F2A743
F7CA91
FBE8D2
FDF5EE

Requirements
Must have
• unique, memorable, not something men have seen over and over again,
Nice to have
• eye catching
Should not have
• Been something I could have made by myself

```html
<!DOCTYPE html>
<html lang="en">
<head>
<meta charset="utf-8">
<title>Summit Renewals – Business Card</title>
<link href="https://fonts.googleapis.com/css2?family=PT+Serif:wght@700&family=Arimo:wght@400&display=swap" rel="stylesheet">
<style>
  :root {
    --page: #dedede;
    --card: #ededed;
    --navy: #0f3049;
    --orange: #e07020;
    --ink: #2b2b2b;
    --white: #f4f4f4;
  }
  * { box-sizing: border-box; margin: 0; padding: 0; }
  html, body {
    width: 1200px;
    height: 1124px;
    overflow: hidden;
    background: var(--page);
  }
  .card {
    position: absolute;
    left: 252px;
    width: 696px;
    height: 398px;
    border-radius: 24px;
    overflow: hidden;
    background: var(--card);
  }
  .card--front { top: 134px; }
  .card--back { top: 593px; }

  .front-art { position: absolute; inset: 0; }

  .brand-name {
    font-family: "PT Serif", Georgia, serif;
    font-weight: 700;
    color: var(--orange);
    text-align: center;
    line-height: 1.02;
    text-transform: uppercase;
  }
  .card--front .brand-name {
    position: absolute;
    left: 470px;
    top: 70px;
    width: 220px;
    font-size: 34px;
  }
  .card--back .brand-name {
    position: absolute;
    left: 0;
    top: 80px;
    width: 100%;
    font-size: 56px;
  }

  .owner {
    position: absolute;
    left: 40px;
    top: 204px;
  }
  .owner__name {
    font-family: "PT Serif", Georgia, serif;
    font-weight: 700;
    font-size: 25px;
    color: var(--orange);
    letter-spacing: 0.2px;
    line-height: 1.1;
  }
  .owner__role {
    font-family: "Arimo", Helvetica, Arial, sans-serif;
    font-size: 18px;
    color: var(--white);
    margin-top: 1px;
  }

  .contact {
    position: absolute;
    left: 40px;
    top: 280px;
    list-style: none;
    font-family: "Arimo", Helvetica, Arial, sans-serif;
    font-size: 17.5px;
    color: var(--white);
  }
  .contact__item {
    display: flex;
    align-items: center;
    height: 28.5px;
  }
  .contact__icon {
    width: 12px;
    height: 12px;
    margin-right: 8px;
    flex: none;
  }

  .services {
    position: absolute;
    left: 0;
    top: 312px;
    width: 100%;
    text-align: center;
    font-family: "Arimo", Helvetica, Arial, sans-serif;
    font-size: 17.5px;
    line-height: 24px;
    color: var(--ink);
  }
  .services__dot {
    color: var(--orange);
    margin: 0 4px 0 8px;
  }
</style>
</head>
<body>

  <section class="card card--front" aria-label="Business card front">
    <svg class="front-art" viewBox="0 0 696 398" width="696" height="398" aria-hidden="true">
      <rect width="696" height="398" fill="var(--navy)"/>
      <path d="M241 0 C280 200, 430 320, 696 334 L696 0 Z" fill="var(--card)"/>
      <path d="M221 0 C256 200, 420 325, 623 325" fill="none" stroke="var(--white)" stroke-width="10"/>
      <path d="M229 0 C263 200, 425 322, 623 325" fill="none" stroke="var(--orange)" stroke-width="6"/>
    </svg>

    <div class="brand-name">Summit<br>Renewals</div>

    <div class="owner">
      <div class="owner__name">DENNIS MORAVEC</div>
      <div class="owner__role">Owner</div>
    </div>

    <ul class="contact">
      <li class="contact__item">
        <svg class="contact__icon" viewBox="0 0 12 12"><path d="M2.2 0.8 L4.2 0.6 L5 3.4 L3.7 4.5 C4.4 6 5.8 7.5 7.5 8.3 L8.6 7 L11.4 7.8 L11.2 9.8 C10.9 11 9.8 11.4 8.6 11 C4.8 9.8 2.2 7.2 1 3.4 C0.6 2.2 1 1.1 2.2 0.8 Z" fill="var(--orange)"/></svg>
        <span>410-386-7294</span>
      </li>
      <li class="contact__item">
        <svg class="contact__icon" viewBox="0 0 12 12"><rect x="0" y="2" width="12" height="8" fill="var(--orange)"/><path d="M0 2 L6 6.6 L12 2" fill="none" stroke="var(--navy)" stroke-width="1"/></svg>
        <span>dmoravec@summitrenewalsqx.example</span>
      </li>
      <li class="contact__item">
        <svg class="contact__icon" viewBox="0 0 12 12" fill="none" stroke="var(--orange)" stroke-width="1.1"><circle cx="6" cy="6" r="5.3"/><ellipse cx="6" cy="6" rx="2.4" ry="5.3"/><path d="M0.7 6 H11.3 M1.5 3.3 H10.5 M1.5 8.7 H10.5"/></svg>
        <span>www.SummitRenewalsQX.example</span>
      </li>
    </ul>
  </section>

  <section class="card card--back" aria-label="Business card back">
    <div class="brand-name">Summit<br>Renewals</div>
    <p class="services">
      Residential<span class="services__dot">•</span>Emergency Response<span class="services__dot">•</span>Board- up<span class="services__dot">•</span>Storm Protection<br>
      Complete Restoration
    </p>
  </section>

</body>
</html>
```